Re-design of Business Card

We require a design for our business card.

Korrim is a supplier of industrial packaging specializing in plastic products. We are undergoing a rebranding to appear more corporate. We have changed our company name to korrim and have a new logo.

I have uploaded our old card design with the previous company name.
Don't copy the current design. We are looking for a new design.

Industry/Entity Type

Manufacturing

Contact Information for Business Card

please don't copy the current design. we are looking for a new design.

Font styles to use
Sans Serif

Colors

Designer to choose colors to be used in the design.

Requirements
Must have
• clean and easy to read.

```html
<!DOCTYPE html>
<html lang="en">
<head>
<meta charset="utf-8">
<title>Korrim Business Card</title>
<link href="https://fonts.googleapis.com/css2?family=Lato:wght@400;700;900&display=swap" rel="stylesheet">
<style>
  :root {
    --orange: #f47b20;
    --ink: #333333;
    --grey: #7a7a7a;
    --white: #ffffff;
    --backdrop: #5b4838;
  }
  * { margin: 0; padding: 0; box-sizing: border-box; }
  html, body { width: 1000px; height: 1200px; overflow: hidden; }
  body {
    background: var(--backdrop);
    font-family: 'Lato', sans-serif;
    position: relative;
  }
  .card {
    position: absolute;
    box-shadow: 0 4px 14px rgba(0,0,0,0.35);
    overflow: hidden;
  }
  .card-front { left: 111px; top: 120px; width: 777px; height: 446px; background: var(--white); }
  .card-back { left: 109px; top: 633px; width: 782px; height: 446px; background: var(--orange); }

  .wordmark {
    position: absolute;
    font-family: 'Lato', sans-serif;
    font-weight: 900;
    letter-spacing: 1px;
    line-height: 1;
  }
  .card-front .wordmark { left: 66px; top: 183px; font-size: 70px; color: var(--orange); }
  .card-back .wordmark { left: 48px; top: 50px; font-size: 64px; color: var(--white); }

  .divider {
    position: absolute; left: 387px; top: 128px;
    width: 2px; height: 192px; background: var(--orange);
  }
  .contact { position: absolute; left: 430px; top: 122px; color: var(--ink); }
  .contact .name { font-size: 24px; font-weight: 700; color: var(--orange); line-height: 28px; }
  .contact .role { font-size: 18px; line-height: 26px; }
  .contact .address { font-size: 18.5px; line-height: 25px; margin-top: 10px; }
  .contact .lines { list-style: none; margin-top: 12px; font-size: 18.5px; }
  .contact .lines li { display: flex; align-items: center; height: 25px; }
  .contact .lines svg { width: 16px; height: 16px; margin-right: 9px; fill: var(--orange); }

  .footer-band { position: absolute; left: 0; bottom: 0; width: 777px; height: 19px; }

  .services { position: absolute; left: 48px; top: 153px; list-style: none; }
  .services li { position: relative; padding-left: 21px; margin-bottom: 8px; }
  .services li::before {
    content: ""; position: absolute; left: 0; top: 8px;
    width: 9px; height: 9px; border-radius: 50%; background: var(--ink);
  }
  .services .heading { font-size: 18px; font-weight: 700; color: var(--ink); line-height: 24px; }
  .services .detail { font-size: 17px; color: var(--white); line-height: 23px; }
</style>
</head>
<body>
  <section class="card card-front">
    <div class="wordmark">KORRIM</div>
    <div class="divider"></div>
    <div class="contact">
      <p class="name">DANIEL HARLOW</p>
      <p class="role">Owner</p>
      <p class="address">18 Brennan Rd North<br>Halden Park, Qld 4172</p>
      <ul class="lines">
        <li><svg viewBox="0 0 16 16"><path d="M3.2 1.5l2.4-.2 1.3 3.2-1.6 1.2c.8 1.7 2 2.9 3.7 3.8l1.2-1.6 3.2 1.3-.2 2.4c-.1.8-.8 1.4-1.6 1.4C6.3 12.8 1.9 8.4 1.8 3.1c0-.8.6-1.5 1.4-1.6z"/></svg>07 3481 2096</li>
        <li><svg viewBox="0 0 16 16"><path d="M1 3.5h14v1.2L8 9 1 4.7z"/><path d="M1 6.3l7 4.3 7-4.3v6.2H1z"/></svg>sales@korrimpack.com.au</li>
        <li><svg viewBox="0 0 16 16" fill="none" stroke="#f47b20" stroke-width="1.3"><circle cx="8" cy="8" r="6.5"/><ellipse cx="8" cy="8" rx="2.8" ry="6.5"/><path d="M1.5 8h13M2.6 4.6h10.8M2.6 11.4h10.8"/></svg>www.korrimpack.com.au</li>
      </ul>
    </div>
    <svg class="footer-band" viewBox="0 0 777 19" preserveAspectRatio="none">
      <polygon points="0,0 388,0 370,19 0,19" fill="#7a7a7a"/>
      <polygon points="396,0 777,0 777,19 378,19" fill="#f47b20"/>
    </svg>
  </section>

  <section class="card card-back">
    <div class="wordmark">KORRIM</div>
    <ul class="services">
      <li><p class="heading">FLEXIBLE PACKAGING</p><p class="detail">Stretch Wrap, Heat Shrink, Poly Bags, Carton Liners, Pallet Bags &amp; Covers.</p></li>
      <li><p class="heading">BUILDING / DEMOLITION PRODUCTS</p><p class="detail">Concrete Underlay and Asbestos Removal Plastics.</p></li>
      <li><p class="heading">LOAD RESTRAINTS</p><p class="detail">Steel, Polyester (PET) Polypropylene strapping consumables, tools and accessories.</p></li>
      <li><p class="heading">TAPES</p><p class="detail">Carton Sealing, Duct Tapes &amp; Masking Tapes.</p></li>
      <li><p class="heading">MACHINERY</p><p class="detail">Pallet Wrapping Machines &amp; Strapping Tools.</p></li>
    </ul>
  </section>
</body>
</html>
```